Lab & Medical Equipment Repair Company Business Card Design

Looking for business card design for a lab & medical equipment repair company. Must be double-sided and must list our primary pieces we repair. Optionally, can include a QR code which should direct to our website.

Clients are usually doctors, so the card must be designed with a professional tone; however, we are looking for creativity in presentation. Open as to what should be on the front and back on card.

** Looking for a CLEAN design with creativity. Please use "Nice to have Priorities" items with discretion.

Core marketing logic:

When lab or medical equipment needs repair, most doctors call the manufacturers and schedule a technician to repair. Usually this takes one or two weeks, and, often, their work spoils. Alternatively, the doctors could hold equipment insurance which gives them a less expensive cost, but the response time is still similarly long.

Our company provides both competitive rates and one of the fastest response times in the industry. Technicians are dispatched directly to the site of the equipment, usually within 24 hours. Equipment under contract receives the same fast response time and includes complimentary annual maintenance. We service some of the most prestigious facilities in the Pittsburgh area and cover all of Western Pennsylvania, Ohio, and West Virginia.

Target Market(s)

Laboratory owners (doctors)

Industry/Entity Type

Marketing

Requirements
Must have
• Company Logo
Employee Name: Ron Kovalenko
Employee Title: CEO
Company Phone: 724-318-6672
Company Fax: 866-791-3058
Company Address: PO Box 571 Harmony Ridge, PA 16094
Company Website: www.brightbenchfixers.example
Equipment We Service: Freezers, Cryostorage, Incubators, Centrifuges, Refrigerators, Environmental Chambers, Autoclaves, and more.

Nice to have
• Company Facebook: facebook.com/bbfllc
Company Twitter: @BBFLLC
QR Code (link to website): www.brightbenchfixers.example

```html
<!DOCTYPE html>
<html lang="en">
<head>
<meta charset="utf-8">
<title>Business Card Design – Bright Bench Fixers</title>
<link rel="stylesheet" href="https://fonts.googleapis.com/css2?family=Arimo:wght@700&family=Montserrat:wght@300;400;600;700&display=swap">
<style>
  :root {
    --ink: #111111;
    --paper: #ffffff;
    --pulse-green: #46e03c;
    --rule: #000000;
  }
  * { margin: 0; padding: 0; box-sizing: border-box; }
  html, body { width: 928px; height: 1200px; overflow: hidden; background: var(--paper); }
  .sheet {
    position: relative;
    width: 928px;
    height: 1200px;
    border: 1px solid var(--rule);
    font-family: "Montserrat", sans-serif;
    color: var(--ink);
  }
  .sheet-title {
    position: absolute;
    left: 76px;
    top: 65px;
    font-family: "Arimo", sans-serif;
    font-weight: 700;
    font-size: 17px;
    line-height: 21px;
  }
  .side-label {
    position: absolute;
    left: 0;
    width: 928px;
    text-align: center;
    font-family: "Arimo", sans-serif;
    font-weight: 700;
    font-size: 17px;
  }
  .side-label--front { top: 301px; }
  .side-label--back { top: 670px; }
  .card {
    position: absolute;
    left: 272px;
    width: 383px;
    height: 219px;
    border: 1px solid var(--rule);
    background: var(--paper);
  }
  .card--front { top: 344px; }
  .card--back { top: 710px; }
  .brand-name {
    position: absolute;
    inset: 0;
    display: flex;
    align-items: center;
    justify-content: center;
    font-weight: 700;
    font-size: 92px;
    letter-spacing: 10px;
    color: var(--ink);
  }
  .services {
    position: absolute;
    left: 18px;
    top: 20px;
    width: 347px;
    color: var(--pulse-green);
    font-weight: 600;
  }
  .services-heading {
    font-size: 11px;
    text-transform: uppercase;
    letter-spacing: 1.5px;
    margin-bottom: 8px;
  }
  .services-list {
    list-style: none;
    display: grid;
    grid-template-columns: repeat(3, auto);
    column-gap: 14px;
    row-gap: 5px;
    font-size: 10.5px;
    line-height: 13px;
  }
  .services-rule {
    position: absolute;
    left: 18px;
    right: 18px;
    top: 136px;
    height: 1px;
    background: var(--pulse-green);
  }
  .contact {
    position: absolute;
    right: 16px;
    top: 148px;
    text-align: right;
    color: var(--ink);
  }
  .contact-name { font-weight: 700; font-size: 11.5px; line-height: 15px; }
  .contact-title { font-weight: 400; }
  .contact-address { font-weight: 300; font-size: 12px; line-height: 15px; }
  .contact-line { font-weight: 400; font-size: 10px; line-height: 13px; }
  .dot { color: var(--pulse-green); }
</style>
</head>
<body>
<main class="sheet">
  <div class="sheet-title">BUSINESS CARD DESIGN<br>size: 3.5”W x 2”H</div>

  <div class="side-label side-label--front">FRONT</div>
  <section class="card card--front" aria-label="Card front">
    <div class="brand-name">BBF</div>
  </section>

  <div class="side-label side-label--back">BACK</div>
  <section class="card card--back" aria-label="Card back">
    <div class="services">
      <p class="services-heading">Equipment We Service:</p>
      <ul class="services-list">
        <li>Freezers</li>
        <li>Cryostorage</li>
        <li>Incubators</li>
        <li>Centrifuges</li>
        <li>Refrigerators</li>
        <li>Autoclaves</li>
        <li>Environmental Chambers</li>
        <li>and more.</li>
      </ul>
    </div>
    <div class="services-rule"></div>
    <div class="contact">
      <p class="contact-name">RON KOVALENKO <span class="dot">•</span> <span class="contact-title">CEO</span></p>
      <p class="contact-address">PO Box 571 Harmony Ridge, PA 16094</p>
      <p class="contact-line">Phone: 724-318-6672 <span class="dot">•</span> Fax: 866-791-3058</p>
      <p class="contact-line">www.brightbenchfixers.example</p>
    </div>
  </section>
</main>
</body>
</html>
```